Brindle Yard Care. The best in the biz

I run a lawn care service that offers full service mowing. 100% satisfaction guarantee. Fast, Friendly, quality service "I am your lawns best friend" I cut residential lawns. I offer a mow package that includes trimming, edging and clean up. Prices very from 20 dollars to 75. I want my logo to stand out. Free estimates

Target Market(s)

Home owners

Industry/Entity Type

Landscaping

Contact Information for Business Card

482-615-0273 tomkerl47@quillmail.net Dorian. Brindle Yard care

Colors
f37122
9bcb3c
cadf82

Requirements
Must have
• Company name.
• Phone number
• Email
• My services
• images
Nice to have
• A sun that is growing grass.
Should not have
• Incorrect information

```html
<!DOCTYPE html>
<html lang="en">
<head>
<meta charset="utf-8">
<title>Brindle Yard Care – Business Card</title>
<link href="https://fonts.googleapis.com/css2?family=Open+Sans:wght@400;600;700&display=swap" rel="stylesheet">
<style>
  :root {
    --bg: #ece9e3;
    --card: #ffffff;
    --green: #2fae4e;
    --green-dark: #3c8a2a;
    --grass-light: #9bcb3c;
    --grass-pale: #cadf82;
    --sun: #f37122;
    --ink: #3a3a3a;
  }
  * { margin: 0; padding: 0; box-sizing: border-box; }
  html, body {
    width: 1200px; height: 1022px; overflow: hidden;
    background: var(--bg);
    font-family: "Open Sans", Arial, sans-serif;
  }
  .business-card {
    position: absolute; left: 100px; top: 225px;
    width: 1000px; height: 572px;
    background: var(--card);
    box-shadow: 0 6px 24px rgba(0,0,0,0.15);
    overflow: hidden;
  }
  .grass-band {
    position: absolute; left: 0; bottom: 0; width: 1000px; height: 170px;
  }
  .owner { position: absolute; left: 64px; top: 56px; }
  .owner-name {
    font-size: 40px; font-weight: 700; color: var(--green);
    letter-spacing: 1px; line-height: 1;
  }
  .owner-role {
    font-size: 22px; color: var(--ink); margin-top: 6px; letter-spacing: 0.5px;
  }
  .contact { list-style: none; margin-top: 12px; }
  .contact li {
    display: flex; align-items: center; gap: 10px;
    font-size: 22px; color: var(--ink); line-height: 1.45;
  }
  .contact svg { width: 18px; height: 18px; flex: none; }
  .services { position: absolute; left: 64px; top: 236px; }
  .services-title {
    font-size: 28px; font-weight: 700; color: var(--green); letter-spacing: 1px;
  }
  .services-list { list-style: none; margin-top: 4px; }
  .services-list li {
    position: relative; padding-left: 26px;
    font-size: 22px; color: var(--ink); line-height: 1.38;
  }
  .services-list li::before {
    content: ""; position: absolute; left: 0; top: 11px;
    width: 11px; height: 11px; border-radius: 50%; background: var(--green);
  }
  .brand {
    position: absolute; left: 540px; top: 70px;
    display: flex; align-items: center; gap: 18px;
  }
  .brand-dot {
    width: 86px; height: 86px; border-radius: 50%;
    background: var(--sun); flex: none;
  }
  .brand-name {
    font-size: 36px; font-weight: 600; color: var(--green-dark); line-height: 1.15;
    white-space: nowrap;
  }
  .tagline {
    position: absolute; left: 580px; top: 250px;
    font-size: 22px; color: var(--green); letter-spacing: 1px;
  }
</style>
</head>
<body>
  <div class="business-card">
    <svg class="grass-band" viewBox="0 0 1000 170" preserveAspectRatio="none" role="img" aria-label="Illustrated band of green grass along the bottom of the card">
      <defs>
        <linearGradient id="grassFill" x1="0" y1="0" x2="0" y2="1">
          <stop offset="0" stop-color="#9bcb3c"/>
          <stop offset="0.55" stop-color="#5fae2e"/>
          <stop offset="1" stop-color="#3c8a2a"/>
        </linearGradient>
      </defs>
      <path d="M0 158 C 250 166, 450 150, 600 118 S 850 30, 1000 10 L1000 170 L0 170 Z" fill="url(#grassFill)"/>
    </svg>

    <div class="owner">
      <div class="owner-name">DORIAN . BRINDLE</div>
      <div class="owner-role">LAWN CARE</div>
      <ul class="contact">
        <li>
          <svg viewBox="0 0 24 24" aria-hidden="true"><path fill="#2fae4e" d="M6.6 10.8a15.1 15.1 0 0 0 6.6 6.6l2.2-2.2a1 1 0 0 1 1-.25 11.4 11.4 0 0 0 3.6.57 1 1 0 0 1 1 1V20a1 1 0 0 1-1 1A17 17 0 0 1 3 4a1 1 0 0 1 1-1h3.5a1 1 0 0 1 1 1c0 1.250.2 2.450.57 3.6a1 1 0 0 1-.25 1z"/></svg>
          482-615-0273
        </li>
        <li>
          <svg viewBox="0 0 24 24" aria-hidden="true"><rect x="2" y="5" width="20" height="14" rx="1.5" fill="none" stroke="#2fae4e" stroke-width="2"/><path d="M3 6l9 7 9-7" fill="none" stroke="#2fae4e" stroke-width="2"/></svg>
          tomkerl47@quillmail.net
        </li>
      </ul>
    </div>

    <div class="services">
      <div class="services-title">SERVICES</div>
      <ul class="services-list">
        <li>100% satisfaction guarantee</li>
        <li>Fast, Friendly, quality service</li>
        <li>Cut residential lawns</li>
        <li>I offer a mow package</li>
        <li>That includes trimming</li>
        <li>Edging and clean up</li>
        <li>Prices very from 20 dollars to 75</li>
      </ul>
    </div>

    <div class="brand">
      <span class="brand-dot"></span>
      <span class="brand-name">Brindle Yard Care</span>
    </div>

    <div class="tagline">I AM YOUR LAWNS BEST FRIEND</div>
  </div>
</body>
</html>
```